Criação de Manual da Marca para Consultoria de Negócios
" Serviço de assinatura de informações para postos de combustíveis, em um mercado onde centavos são relevantes, a plataforma lumitra vendas vem ao encontro de atender o processo de precificação para os donos, gestores de postos de combustíveis. "

```html
<!DOCTYPE html>
<html lang="pt-BR">
<head>
<meta charset="UTF-8">
<title>Lumitra Vendas — Manual da Marca</title>
<link rel="stylesheet" href="https://fonts.googleapis.com/css2?family=Montserrat:wght@700;800;900&family=Open+Sans:wght@400;600&display=swap">
<style>
  :root {
    --navy: #1f3a6b;
    --navy-deep: #162c54;
    --orange: #f07a1a;
    --yellow: #f4d21a;
    --green: #3fb34a;
    --paper: #f7f7f5;
    --ink: #5c6470;
    --backdrop: #e4e5e6;
  }
  * { box-sizing: border-box; margin: 0; padding: 0; }
  html, body { width: 1200px; height: 1200px; overflow: hidden; }
  body { background: var(--backdrop); font-family: "Open Sans", sans-serif; color: var(--ink); position: relative; }

  .spread { position: absolute; left: 50px; top: 290px; width: 1100px; height: 580px; display: flex; box-shadow: 0 10px 30px rgba(0,0,0,.12); }
  .page { position: relative; width: 550px; height: 580px; background: var(--paper); overflow: hidden; }
  .page--left { background: linear-gradient(90deg, var(--paper) 92%, #e9e9e7 100%); }
  .page--right { background: linear-gradient(90deg, #e9e9e7 0%, var(--paper) 8%); }

  .top-band { position: absolute; left: 0; top: 0; width: 100%; height: 16px; }
  .bottom-band { position: absolute; left: 0; bottom: 0; width: 100%; height: 52px; }

  .chapter-number { position: absolute; top: 30px; left: 30px; font-family: "Montserrat", sans-serif; font-weight: 900; font-size: 30px; color: var(--orange); }
  .intro { position: absolute; top: 30px; left: 92px; width: 430px; font-size: 9px; line-height: 1.45; }

  .section-title { position: absolute; left: 30px; font-family: "Montserrat", sans-serif; font-weight: 900; color: var(--navy); font-size: 27px; line-height: 1.05; padding-left: 22px; }
  .section-title::before { content: ""; position: absolute; left: 0; top: 7px; width: 13px; height: 13px; background: var(--orange); }

  .body-text { position: absolute; font-size: 10px; line-height: 1.5; }

  .tile { position: absolute; display: flex; align-items: center; justify-content: center; }
  .tile--yellow { background: var(--yellow); }
  .tile--green { background: var(--green); }
  .tile--white { background: #ffffff; border: 1px solid #e1e2e4; }
  .tile--navy { background: var(--navy); }
  .photo-fuel-a { background: linear-gradient(135deg, #7d8a4a 0%, #c8b46a 45%, #b82a22 100%); }
  .photo-fuel-b { background: linear-gradient(135deg, #c9ccd0 0%, #d8b43a 50%, #b5221c 100%); }

  .brand { display: inline-flex; align-items: center; gap: 5px; font-family: "Montserrat", sans-serif; font-weight: 800; letter-spacing: .02em; white-space: nowrap; line-height: 1; }
  .brand::before { content: ""; flex: none; width: .8em; height: .8em; background: currentColor; }
  .brand--navy { color: var(--navy); }
  .brand--orange { color: var(--orange); }
  .brand--white { color: #ffffff; }
  .brand--stacked { gap: .35em; line-height: 1.05; }
  .brand--stacked::before { width: 1.1em; height: 1.1em; }

  .dollar-icon { position: absolute; left: 32px; top: 236px; width: 26px; height: 34px; font-family: "Montserrat", sans-serif; font-weight: 900; font-size: 30px; color: var(--orange); line-height: 34px; text-align: center; }

  .mini-logo { position: absolute; }
  .caption { font-size: 8px; line-height: 1.35; margin-top: 5px; }
  .note { position: absolute; font-size: 8.5px; line-height: 1.45; width: 200px; }

  .size-row { position: absolute; left: 30px; width: 490px; display: flex; align-items: flex-end; justify-content: space-between; }
  .size-item { display: flex; flex-direction: column; align-items: center; }
  .size-label { font-size: 7px; margin-top: 4px; border-top: 1px solid var(--ink); padding-top: 1px; }

  .cover-brand { position: absolute; left: 0; right: 0; top: 1000px; text-align: center; }
  .cover-brand .brand { font-size: 30px; }
</style>
</head>
<body>

<main class="spread">
  <section class="page page--left">
    <svg class="top-band" viewBox="0 0 550 16" preserveAspectRatio="none">
      <rect width="550" height="16" fill="var(--navy)"/>
      <polygon points="430,0 550,0 550,6 440,6" fill="var(--orange)"/>
    </svg>

    <div class="chapter-number">05</div>
    <p class="intro">Este capítulo apresenta as regras de aplicação da marca em diferentes superfícies, garantindo leitura clara e presença consistente em todos os materiais do posto.</p>

    <h2 class="section-title" style="top:116px;">APLICAÇÃO<br>SOBRE FUNDOS</h2>

    <p class="body-text" style="left:30px; top:200px; width:230px;">A orientação para o uso da logomarca sobre fundos (gráfico ou fotografia) é de acordo com a legibilidade, o reconhecimento da sua forma.</p>
    <p class="body-text" style="left:300px; top:200px; width:220px;">Em fundos onde não garantimos uma leitura adequada, deveremos utilizar as versões monocromáticas da logomarca.</p>

    <div class="tile tile--yellow" style="left:36px; top:294px; width:140px; height:94px;"><span class="brand brand--navy" style="font-size:11px;">LUMITRA VENDAS</span></div>
    <div class="tile tile--green" style="left:186px; top:294px; width:128px; height:94px;"><span class="brand brand--white" style="font-size:10px;">LUMITRA VENDAS</span></div>
    <div class="tile photo-fuel-a" role="img" aria-label="Fotografia de mão abastecendo um carro vermelho com bomba de combustível" style="left:324px; top:294px; width:150px; height:94px;"></div>

    <div class="tile tile--white" style="left:36px; top:400px; width:140px; height:106px;"><span class="brand brand--orange" style="font-size:11px;">LUMITRA VENDAS</span></div>
    <div class="tile tile--navy" style="left:186px; top:400px; width:128px; height:106px;"><span class="brand brand--white" style="font-size:10px;">LUMITRA VENDAS</span></div>
    <div class="tile photo-fuel-b" role="img" aria-label="Fotografia de bico de bomba amarelo abastecendo um carro vermelho" style="left:324px; top:400px; width:150px; height:106px;"></div>

    <svg class="bottom-band" viewBox="0 0 550 52" preserveAspectRatio="none">
      <polygon points="0,30 550,30 550,52 0,52" fill="var(--navy)"/>
      <polygon points="420,30 550,12 550,30" fill="var(--orange)"/>
      <polygon points="470,52 550,40 550,52" fill="var(--orange)"/>
    </svg>
  </section>

  <section class="page page--right">
    <svg class="top-band" viewBox="0 0 550 16" preserveAspectRatio="none">
      <rect width="550" height="16" fill="var(--navy)"/>
      <polygon points="0,0 120,0 110,6 0,6" fill="var(--orange)"/>
    </svg>

    <div class="chapter-number">05</div>
    <p class="intro">As orientações desta seção mostram como a marca mantém sua força em qualquer formato, do impresso ao digital, sem perder clareza.</p>

    <h2 class="section-title" style="top:150px;">REDEUÇÃO</h2>

    <p class="body-text" style="left:30px; top:194px; width:470px;">Para garantir a boa leitura do logotipo, os estudos realizados mostraram que o mínimo não poderá ser aplicado com dimensões inferiores às medidas abaixo:</p>

    <div class="dollar-icon" aria-hidden="true">$</div>

    <div class="mini-logo" style="left:30px; top:282px;">
      <div class="caption">Impresso: 3 cm<br>Digital: 90 px</div>
    </div>
    <div class="mini-logo" style="left:300px; top:240px;">
      <span class="brand brand--navy" style="font-size:9px;">LUMITRA VENDAS</span>
      <div class="caption">Impresso: 2 cm<br>Digital: 60 px</div>
    </div>

    <p class="note" style="left:30px; top:316px;">Versão colorida usada em peças com área ampla e boa visibilidade.</p>
    <p class="note" style="left:300px; top:316px;">Versão reduzida usada em etiquetas, ícones e pequenos formatos digitais.</p>

    <div class="size-row" style="top:350px;">
      <div class="size-item"><span class="brand brand--navy brand--stacked" style="font-size:5px;">LUMITRA<br>VENDAS</span><span class="size-label">1,0 cm</span></div>
      <div class="size-item"><span class="brand brand--navy brand--stacked" style="font-size:6px;">LUMITRA<br>VENDAS</span><span class="size-label">1,5 cm</span></div>
      <div class="size-item"><span class="brand brand--navy brand--stacked" style="font-size:7px;">LUMITRA<br>VENDAS</span><span class="size-label">2,0 cm</span></div>
      <div class="size-item"><span class="brand brand--navy brand--stacked" style="font-size:8px;">LUMITRA<br>VENDAS</span><span class="size-label">2,5 cm</span></div>
      <div class="size-item"><span class="brand brand--navy brand--stacked" style="font-size:9px;">LUMITRA<br>VENDAS</span><span class="size-label">3,0 cm</span></div>
      <div class="size-item"><span class="brand brand--navy brand--stacked" style="font-size:10px;">LUMITRA<br>VENDAS</span><span class="size-label">3,5 cm</span></div>
    </div>

    <div class="size-row" style="top:420px;">
      <div class="size-item"><span class="brand brand--navy brand--stacked" style="font-size:10px;">LUMITRA<br>VENDAS</span><span class="size-label">4,0 cm</span></div>
      <div class="size-item"><span class="brand brand--navy brand--stacked" style="font-size:11px;">LUMITRA<br>VENDAS</span><span class="size-label">4,5 cm</span></div>
      <div class="size-item"><span class="brand brand--navy brand--stacked" style="font-size:12px;">LUMITRA<br>VENDAS</span><span class="size-label">5,0 cm</span></div>
      <div class="size-item"><span class="brand brand--navy brand--stacked" style="font-size:12.5px;">LUMITRA<br>VENDAS</span><span class="size-label">5,5 cm</span></div>
      <div class="size-item"><span class="brand brand--navy brand--stacked" style="font-size:13px;">LUMITRA<br>VENDAS</span><span class="size-label">6,0 cm</span></div>
    </div>

    <svg class="bottom-band" viewBox="0 0 550 52" preserveAspectRatio="none">
      <polygon points="0,30 550,30 550,52 0,52" fill="var(--navy)"/>
      <polygon points="0,12 130,30 0,30" fill="var(--orange)"/>
      <polygon points="0,40 80,52 0,52" fill="var(--orange)"/>
    </svg>
  </section>
</main>

<div class="cover-brand"><span class="brand brand--navy">LUMITRA VENDAS</span></div>

</body>
</html>
```